K&T Fixit and Rebuild general contracting business card design

I already have a logo that I want to use and I need a card that uses that logo and color scheme on the front with the address phone numbers and email and on the back a place for technicians to write in their name and phone number when they hand it out. It will need the License number of License #KTFXTRB318QN.
It should say General Contractor under the company name. The address is
4417 NE 3rd Ave, Ste D246
Vancouver, WA 98612
www.kandtfixitandrebuild.example
office@kandtfixitandrebuild.example
360-555-0182 is the telephone number
360-555-0149 is the fax number

Target Market(s)

Homeowners needing remodel work or repairs in their home.

Industry/Entity Type

Construction

Contact Information for Business Card

Business name, address, phone number, license number, fax number, email, and website on the front and a place to fill in technician's name and number

Font styles to use
Serif

Requirements
Must have
• Business name, address, phone number, license number, fax number, email, and website on the front and a place to fill in technician's name and number
Nice to have
• I uploaded an example of a front that is good.
Should not have
• Froo froo or extra embellishments.

```html
<!DOCTYPE html>
<html lang="en">
<head>
<meta charset="utf-8">
<title>K&amp;T Fixit and Rebuild – Business Card</title>
<link rel="stylesheet" href="https://fonts.googleapis.com/css2?family=PT+Serif:wght@400;700&display=swap">
<style>
  :root {
    --backdrop: #d3d3d3;
    --wood-dark: #6e3a1c;
    --wood-mid: #9a5a2e;
    --wood-light: #b8733f;
    --panel: #ffffff;
    --ink: #111111;
    --navy: #1c2b4d;
    --copper: #a55a2c;
    --logo-light: #ffffff;
  }
  * { margin: 0; padding: 0; box-sizing: border-box; }
  html, body {
    width: 1200px; height: 1000px; overflow: hidden;
    background: var(--backdrop);
    font-family: "PT Serif", Georgia, serif;
    color: var(--ink);
  }
  .canvas { position: relative; width: 1200px; height: 1000px; }
  .card { position: absolute; width: 628px; height: 362px; overflow: hidden; }
  .card--front { left: 84px; top: 105px; }
  .card--back { left: 486px; top: 545px; }
  .wood {
    position: absolute; inset: 0;
    background:
      repeating-linear-gradient(90deg, rgba(40,18,6,0.55) 0 2px, transparent 2px 42px),
      linear-gradient(90deg, var(--wood-mid), var(--wood-light) 30%, var(--wood-mid) 55%, var(--wood-light) 80%, var(--wood-dark));
  }
  .front-brand {
    position: absolute; left: 0; right: 0; top: 128px;
    text-align: center; color: var(--logo-light);
  }
  .front-brand__name { font-weight: 700; font-size: 48px; line-height: 1.1; }
  .front-brand__tagline { margin-top: 12px; font-weight: 700; font-size: 22px; letter-spacing: 3px; text-transform: uppercase; }
  .panel {
    position: absolute; left: 44px; top: 25px; width: 540px; height: 312px;
    background: var(--panel);
  }
  .back-brand {
    position: absolute; right: 26px; top: 24px; width: 140px;
    color: var(--copper); text-align: center;
  }
  .back-brand__name { font-weight: 700; font-size: 19px; line-height: 1.15; }
  .back-brand__tagline { margin-top: 4px; font-weight: 700; font-size: 10px; letter-spacing: 1px; text-transform: uppercase; }
  .fill-in { position: absolute; left: 28px; top: 44px; }
  .fill-in__row { display: flex; align-items: flex-end; height: 23px; }
  .fill-in__label { width: 74px; font-weight: 700; font-size: 16px; line-height: 1; }
  .fill-in__line { width: 248px; border-bottom: 2px solid var(--navy); margin-bottom: 2px; }
  .license { position: absolute; left: 28px; top: 99px; font-size: 19px; letter-spacing: 0.3px; }
  .contact-list { position: absolute; left: 28px; top: 151px; list-style: none; }
  .contact-list li { display: flex; align-items: flex-start; font-size: 16px; line-height: 24px; }
  .contact-list svg { width: 16px; height: 16px; margin: 4px 9px 0 0; flex: none; fill: var(--navy); }
</style>
</head>
<body>
<main class="canvas">
  <section class="card card--front">
    <div class="wood" role="img" aria-label="Warm brown vertical wood plank background"></div>
    <div class="front-brand">
      <div class="front-brand__name">K&amp;T Fixit and Rebuild</div>
      <div class="front-brand__tagline">General Contractor</div>
    </div>
  </section>

  <section class="card card--back">
    <div class="wood" role="img" aria-label="Warm brown vertical wood plank background"></div>
    <div class="panel">
      <div class="back-brand">
        <div class="back-brand__name">K&amp;T Fixit<br>and Rebuild</div>
        <div class="back-brand__tagline">General Contractor</div>
      </div>
      <div class="fill-in">
        <div class="fill-in__row"><span class="fill-in__label">Name:</span><span class="fill-in__line"></span></div>
        <div class="fill-in__row"><span class="fill-in__label">Contact:</span><span class="fill-in__line"></span></div>
      </div>
      <div class="license">#KTFXTRB318QN</div>
      <ul class="contact-list">
        <li><svg viewBox="0 0 16 16"><path d="M1 5c0-2 3-3 7-3s7 1 7 3v1h-4V5H5v1H1z"/><path d="M3 7h10l1 7H2z M6 9h4v3H6z" fill-rule="evenodd"/></svg>360-555-0182</li>
        <li><svg viewBox="0 0 16 16"><path d="M4 1h8v4H4z"/><path d="M1 6h14v9H1z M4 9h8v3H4z" fill-rule="evenodd"/></svg>360-555-0149</li>
        <li><svg viewBox="0 0 16 16"><path d="M8 0a5 5 0 0 1 5 5c0 4-5 11-5 11S3 9 3 5a5 5 0 0 1 5-5zm0 3a2 2 0 1 0 0 4 2 2 0 0 0 0-4z"/></svg><span>4417 NE 3rd Ave, Ste D246<br>Vancouver, WA 98612</span></li>
        <li><svg viewBox="0 0 16 16"><path d="M1 4h14v1L8 9 1 5z"/><path d="M1 6.5l7 4 7-4V13H1z"/></svg>office@kandtfixitandrebuild.example</li>
        <li><svg viewBox="0 0 16 16"><path d="M8 1a7 7 0 1 0 0 14A7 7 0 0 0 8 1zm-3 4h3l1 2-2 2 1 3-2 1-1-3-2-1 1-3zm6 1 2 2-1 3-2-1 1-2z"/></svg>www.kandtfixitandrebuild.example</li>
      </ul>
    </div>
  </section>
</main>
</body>
</html>
```